BrightLoop - IT services company
Refresh Stationary
Project: BrightLoop - IT services company
BrightLoop  - IT services company -
Creative Brief
Simple
Delia Okonjo
Marketing Manager
2418 Fenwick Lane Suite 140 Durham, NC 27705
delia.okonjo@brightloop-example.com
www.brightloop-example.com

```html
<!DOCTYPE html>
<html lang="en">
<head>
<meta charset="utf-8">
<title>BrightLoop Business Card</title>
<link rel="stylesheet" href="https://fonts.googleapis.com/css2?family=Arimo:wght@400;700&display=swap">
<style>
  :root {
    --navy: #1d4f91;
    --orange: #f26a21;
    --ink: #3a3a3a;
    --muted: #7a7a7a;
    --paper: #ffffff;
    --backdrop: #ecebe8;
    --rule: #d9d9d9;
  }
  * { box-sizing: border-box; margin: 0; padding: 0; }
  html, body { width: 1200px; height: 901px; overflow: hidden; }
  body {
    background: var(--backdrop);
    font-family: "Arimo", Arial, sans-serif;
    position: relative;
  }
  .card {
    position: absolute;
    top: 325px;
    width: 460px;
    height: 262px;
    box-shadow: 0 6px 18px rgba(0,0,0,0.18);
    overflow: hidden;
  }
  .card-front { left: 100px; background: var(--paper); }
  .card-back { left: 640px; background: var(--navy); }

  .brand {
    position: absolute;
    display: flex;
    align-items: center;
    gap: 9px;
    font-weight: 700;
    letter-spacing: 0.2px;
  }
  .brand-dot { width: 18px; height: 18px; border-radius: 50%; }
  .card-front .brand { top: 38px; right: 34px; font-size: 26px; color: var(--navy); }
  .card-front .brand-dot { background: var(--orange); }
  .card-back .brand {
    top: 50%; left: 50%; transform: translate(-50%, -50%);
    font-size: 32px; color: var(--paper);
  }
  .card-back .brand-dot { background: var(--paper); width: 22px; height: 22px; }

  .person { position: absolute; left: 30px; top: 88px; }
  .person-name { font-size: 17px; font-weight: 700; color: var(--navy); }
  .person-title { font-size: 10px; color: var(--muted); margin-top: 3px; }

  .contact {
    position: absolute;
    left: 30px;
    bottom: 30px;
    list-style: none;
    font-size: 8.5px;
    line-height: 12px;
    color: var(--ink);
  }
  .contact .label { color: var(--orange); font-weight: 700; }

  .base-rule {
    position: absolute; left: 0; right: 0; bottom: 10px;
    height: 2px; background: var(--rule);
  }
  .base-band {
    position: absolute; left: 0; right: 0; bottom: 0;
    height: 8px; background: var(--navy);
  }
</style>
</head>
<body>
  <section class="card card-front" aria-label="Business card front">
    <div class="brand"><span class="brand-dot"></span>BrightLoop</div>
    <div class="person">
      <p class="person-name">Delia Okonjo</p>
      <p class="person-title">Marketing Manager</p>
    </div>
    <ul class="contact">
      <li>2418 Fenwick Lane, Suite 140</li>
      <li>Durham, NC 27705</li>
      <li><span class="label">Toll Free:</span> 800-555-0147</li>
      <li><span class="label">P:</span> 919-555-0182 &nbsp;<span class="label">F:</span> 919-555-0163</li>
      <li><span class="label">C:</span> 919-555-0129</li>
      <li><span class="label">E:</span> delia.okonjo@brightloop-example.com</li>
      <li>www.brightloop-example.com</li>
    </ul>
    <div class="base-rule"></div>
    <div class="base-band"></div>
  </section>

  <section class="card card-back" aria-label="Business card back">
    <div class="brand"><span class="brand-dot"></span>BrightLoop</div>
  </section>
</body>
</html>
```